Business Card

We are looking to re-create our business card. Attached is the company logo. we would like it to be back and front. for example one side with the persons information and the other side with the company logo. Be as creative as you would like but also keep in mind, we are a Health Insurance company and we need to look professional as well.
Business

```html
<!DOCTYPE html>
<html lang="en">
<head>
<meta charset="utf-8">
<title>Meridian Health Benefits — Business Card</title>
<link rel="stylesheet" href="https://fonts.googleapis.com/css2?family=Open+Sans:wght@400;600;700&display=swap">
<style>
  :root {
    --page: #f2f2f2;
    --card-light: #f4f4f4;
    --brand-blue: #0b86c6;
    --ink-grey: #6d6e71;
    --ink-dark: #55565a;
    --rule: #c9c9c9;
    --white: #ffffff;
    --social-grey: #b9c2c9;
  }
  * { box-sizing: border-box; margin: 0; padding: 0; }
  html, body {
    width: 1200px; height: 900px; overflow: hidden;
    background: var(--page);
    font-family: "Open Sans", Arial, sans-serif;
  }
  .canvas {
    width: 1200px; height: 900px;
    display: flex; flex-direction: column;
    align-items: center; justify-content: center; gap: 60px;
  }
  .card {
    position: relative;
    width: 630px; height: 360px;
    box-shadow: 0 2px 10px rgba(0,0,0,0.12);
  }
  .card-front { background: var(--card-light); color: var(--ink-grey); }
  .card-back { background: var(--brand-blue); color: var(--white); }

  .brand {
    display: flex; align-items: center; gap: 12px;
    font-weight: 600; font-size: 26px; letter-spacing: 0.2px;
  }
  .brand-mark { width: 14px; height: 14px; flex: none; }
  .card-front .brand { position: absolute; left: 56px; top: 58px; color: var(--brand-blue); }
  .card-front .brand-mark { background: var(--ink-grey); }
  .card-back .brand { position: absolute; left: 56px; bottom: 58px; color: var(--white); }
  .card-back .brand-mark { background: var(--white); }

  .brand-rule {
    position: absolute; left: 56px; top: 108px;
    width: 120px; height: 2px; background: var(--rule);
  }

  .social {
    position: absolute; right: 48px; top: 62px;
    display: flex; gap: 6px;
  }
  .social span { width: 20px; height: 20px; background: var(--social-grey); }
  .social span:nth-child(2) { background: #5aa9dc; }
  .social span:nth-child(3) { background: #4d6aa6; }
  .social span:nth-child(4) { background: #2f7bb5; }

  .person { position: absolute; left: 56px; top: 168px; }
  .person-name {
    font-weight: 700; font-size: 19px; color: var(--ink-dark);
    text-transform: uppercase; letter-spacing: 0.5px;
  }
  .person-title { font-size: 14px; color: var(--brand-blue); margin-top: 2px; }
  .contact-list { list-style: none; margin-top: 12px; }
  .contact-list li {
    display: flex; align-items: center; gap: 10px;
    font-size: 14px; line-height: 24px;
  }
  .contact-list svg { width: 14px; height: 14px; flex: none; }
  .address { font-size: 14px; margin-top: 10px; }
</style>
</head>
<body>
<main class="canvas">

  <section class="card card-front" aria-label="Card front">
    <div class="brand"><span class="brand-mark"></span>Meridian Health Benefits</div>
    <div class="brand-rule"></div>

    <div class="social" aria-label="Social links">
      <span></span><span></span><span></span><span></span>
    </div>

    <div class="person">
      <p class="person-name">Daniel Reyes</p>
      <p class="person-title">President</p>
      <ul class="contact-list">
        <li>
          <svg viewBox="0 0 14 14" aria-hidden="true">
            <rect width="14" height="14" rx="2" fill="#0b86c6"/>
            <path d="M4 3.5l1.6 0 .7 2-1 .8a6 6 0 0 0 2.4 2.4l.8-1 2 .7v1.6c-3.5.5-7-3-6.5-6.5z" fill="#fff"/>
          </svg>615.555.0142
        </li>
        <li>
          <svg viewBox="0 0 14 14" aria-hidden="true">
            <rect width="14" height="14" rx="2" fill="#0b86c6"/>
            <rect x="3" y="4.5" width="8" height="5.5" fill="none" stroke="#fff" stroke-width="1"/>
            <path d="M3 4.5l4 3 4-3" fill="none" stroke="#fff" stroke-width="1"/>
          </svg>hello@meridianhb.com
        </li>
        <li>
          <svg viewBox="0 0 14 14" aria-hidden="true">
            <rect width="14" height="14" rx="2" fill="#0b86c6"/>
            <circle cx="7" cy="7" r="4" fill="none" stroke="#fff" stroke-width="1"/>
            <path d="M3 7h8M7 3c-2 2.5-2 5.5 0 8M7 3c2 2.5 2 5.5 0 8" fill="none" stroke="#fff" stroke-width="0.8"/>
          </svg>www.meridianhb.com
        </li>
      </ul>
      <p class="address">48 Linden Row, Franklin TN 37064</p>
    </div>
  </section>

  <section class="card card-back" aria-label="Card back">
    <div class="brand"><span class="brand-mark"></span>Meridian Health Benefits</div>
  </section>

</main>
</body>
</html>
```